Webdesign für Getränkelogistik & Full-Service-Partner bei Events
Zielgruppe
Getränkelogistiker und Full-Service-Partner bei Events
Zielgruppe: Getränke-EinzelHändler; Veranstalter von Events und privaten Feiern
Aufgabenstellung
- soll „Frische“ und „Moderne“ vermitteln, ohne eine Getränkeart in den Vordergrund zu rücken
- soll von den Farben her gut zum Logo passen (siehe Anlagen)
- Slider wäre wünschenswert
- Slogan 'Wir freuen uns auf Sie!'

```html
<!DOCTYPE html>
<html lang="en">
<head>
<meta charset="utf-8">
<title>Nordquell Getränke GmbH</title>
<link href="https://fonts.googleapis.com/css2?family=Cabin:wght@400;500;700&display=swap" rel="stylesheet">
<style>
:root{
  --green:#1f6b5c;
  --green-dark:#17574b;
  --yellow:#f7c414;
  --grey-bg:#f4f4f4;
  --text:#5c5c5c;
  --text-dark:#3f3f3f;
  --white:#ffffff;
}
html,body{margin:0;padding:0;overflow:hidden;}
body{font-family:"Cabin",sans-serif;color:var(--text);background:var(--white);}
.page{position:relative;width:1200px;height:2775px;overflow:hidden;background:var(--white);}
.abs{position:absolute;}
.hero{left:0;top:0;width:1200px;height:600px;background:linear-gradient(180deg,#2d6e5a 0%,#3f8a6e 35%,#2b6b58 70%,#1f5a4c 100%);}
.hero-photo{left:0;top:0;width:1200px;height:600px;background:radial-gradient(ellipse at 30% 40%,rgba(120,170,150,.55),transparent 60%),radial-gradient(ellipse at 75% 30%,rgba(100,150,130,.5),transparent 55%);}
.tagline{right:102px;top:0;font-size:15px;color:var(--white);}
.nav-bar{left:92px;top:22px;width:1015px;height:79px;background:var(--white);border-radius:8px;box-shadow:0 2px 6px rgba(0,0,0,.2);}
.brand{left:22px;top:18px;display:flex;align-items:center;gap:10px;font-size:27px;font-weight:700;color:var(--green);}
.brand-dot{width:28px;height:28px;border-radius:50%;background:var(--yellow);}
.nav{right:16px;top:30px;display:flex;gap:28px;font-size:13.5px;color:var(--green);}
.hero-title{left:0;width:1200px;top:262px;text-align:center;font-size:35px;line-height:41px;font-weight:700;color:var(--yellow);text-shadow:0 2px 4px rgba(0,0,0,.45);text-transform:uppercase;}
.hero-sub{left:0;width:1200px;top:360px;text-align:center;font-size:19px;color:var(--white);}
.dots{left:555px;top:548px;display:flex;gap:10px;}
.dots span{width:10px;height:10px;border-radius:50%;background:var(--white);}
.dots span+span{background:var(--yellow);}
.waves{left:0;top:0;}
h2{margin:0;font-weight:400;font-size:24px;color:var(--green);text-transform:uppercase;}
h2 b{font-weight:700;}
.welcome-h{left:0;width:1200px;top:664px;text-align:center;}
.welcome{left:200px;width:800px;top:723px;text-align:center;font-size:15.5px;line-height:20.5px;color:var(--text-dark);}
.welcome p{margin:0 0 19px;}
.portrait{left:111px;top:1148px;width:292px;height:292px;background:linear-gradient(135deg,#e9e060,#d8cf3a 50%,#c7c0a0);}
.way-h{left:441px;top:1145px;}
.way{left:447px;width:621px;top:1192px;font-size:15.5px;line-height:20px;text-align:justify;}
.way p,.promise p{margin:0 0 20px;}
.promise-h{left:136px;top:1672px;}
.promise{left:136px;width:525px;top:1718px;font-size:15.5px;line-height:20px;text-align:justify;}
.girl{left:740px;top:1555px;width:365px;height:515px;background:linear-gradient(180deg,#c8a07a 0%,#d9b494 30%,#a9a9a9 55%,#5f7fa6 100%);border-radius:180px 180px 20px 20px;}
.testi-h{left:0;width:1200px;top:2088px;text-align:center;}
.card{top:2137px;width:260px;text-align:center;}
.avatar{margin:0 auto;width:106px;height:106px;border-radius:50%;background:radial-gradient(circle at 50% 45%,#c9a48a,#7a5a48);}
.card h3{margin:23px 0 0;font-size:15px;font-weight:500;color:var(--green);}
.card .place{font-size:15px;color:#777;margin-top:0;}
.card p{margin:22px 0 0;font-size:14px;line-height:17.5px;color:#888;}
.quick-h{left:92px;top:2550px;font-size:16px;font-weight:700;color:var(--green);}
.links{top:2594px;font-size:14px;line-height:29.5px;color:#888;}
.contact{left:700px;top:2594px;font-size:14px;color:#888;}
.contact .row{display:flex;gap:10px;align-items:flex-start;}
.stay{left:936px;top:2594px;font-size:14px;color:var(--green);}
.social{display:flex;gap:26px;margin-top:16px;}
.social span{width:18px;height:18px;border-radius:50%;background:var(--green);}
</style>
</head>
<body>
<div class="page">
  <div class="abs hero" role="img" aria-label="Blurred photo of beverage shelves in a drinks market"></div>
  <div class="abs hero-photo"></div>
  <div class="abs tagline">We look forward to seeing you!</div>
  <div class="abs nav-bar">
    <div class="abs brand"><span class="brand-dot"></span>Nordquell</div>
    <nav class="abs nav"><span>Companies</span><span>Team Wholesale</span><span>All about your event</span><span>Career</span><span>Downloads</span><span>Contact</span><span>Data protection / imprint</span></nav>
  </div>
  <div class="abs hero-title">Beverage logistics &amp;<br>full-service partner for events</div>
  <div class="abs hero-sub">We deliver first-class goods to the agreed place at the right time.</div>

  <svg class="abs waves" width="1200" height="2775" viewBox="0 0 1200 2775">
    <path d="M0 568 C200 545 400 540 560 565 C700 585 860 540 1000 560 C1080 570 1150 590 1200 610 L1200 2775 L0 2775 Z" fill="#fff"/>
    <path d="M0 585 C150 565 380 560 540 572 C400 600 200 605 0 600 Z" fill="#f7c414"/>
    <path d="M1030 595 C1100 580 1160 550 1200 520 L1200 655 C1130 630 1080 605 1030 595 Z" fill="#f7c414"/>
    <path d="M0 1090 C250 1080 500 1050 750 1040 C950 1030 1100 1080 1200 1110 L1200 1510 C1000 1560 800 1560 600 1530 C400 1500 200 1520 0 1510 Z" fill="#f4f4f4"/>
    <path d="M290 1104 C360 1094 420 1090 470 1092 C400 1100 340 1104 290 1104 Z" fill="#f7c414"/>
    <path d="M1120 1138 C1150 1128 1175 1120 1200 1115 L1200 1160 C1170 1150 1145 1142 1120 1138 Z" fill="#1f6b5c"/>
    <path d="M120 1505 C240 1490 380 1492 490 1505 C380 1520 240 1520 120 1505 Z" fill="#f7c414"/>
    <path d="M0 2070 C250 2020 450 2005 650 2015 C850 2025 1050 2060 1200 2050 L1200 2500 C1000 2520 800 2500 600 2520 C400 2540 200 2530 0 2520 Z" fill="#f4f4f4"/>
    <path d="M0 2105 C40 2100 70 2094 100 2092 C70 2102 35 2112 0 2120 Z" fill="#f7c414"/>
    <path d="M700 2470 C800 2458 900 2458 1005 2468 C900 2485 800 2485 700 2470 Z" fill="#1f6b5c"/>
    <path d="M960 2775 C1050 2765 1130 2760 1200 2760 L1200 2775 Z" fill="#f7c414"/>
  </svg>

  <h2 class="abs welcome-h">Welcome to <b>Nordquell Getränke GmbH</b></h2>
  <div class="abs welcome">
    <p>From a small bottled beer store to a beverage logistics company - always close to the customer</p>
    <p>When our family business was founded in 1932, the world was different. A lot has happened since then. Our company was also subject to constant change and realigned itself several times.</p>
    <p>But despite all the changes, we at drinks Nordquell have retained the crucial point: reliability and commitment are paramount, we keep our promises - you can rely on us. We act with foresight.</p>
    <p>Our services are exclusively geared towards delivering added value and benefits to our many customers and business partners. Satisfied customers and partners are and remain the best recommendation for us.</p>
    <p>Thank you for your trust and your loyalty!<br>Mara Lindner, managing director</p>
  </div>

  <div class="abs portrait" role="img" aria-label="Portrait photo of the managing director in front of a yellow wall"></div>
  <h2 class="abs way-h">The <b>way</b> to the <b>present</b></h2>
  <div class="abs way">
    <p>More than eighty years is a long time. 1932 by Anton Lindner in Eichwalde. Founded as a bottled beer trade, our company was initially a classic one-man business.</p>
    <p>In 1952 the company was realigned as a food retailer. In 1982 Konrad Lindner took over his father's grocery. In 1990 this grocery store became a FRISCHMARKT store, which is still part of the entire company. In 1994 Konrad Lindner opened his first beverage pick-up market with the "Drink Corner" in Brunnhain, and in 1995 he founded the beverage wholesaler Beverages Nordquell.</p>
    <p>In 1999 the company moved to Talwiese business park - our modern location today. Konrad Lindner died unexpectedly in 2012 at the peak of his creative power. Since then, his wife Mara Lindner has been running the company.</p>
  </div>

  <h2 class="abs promise-h">Our service <b>promise</b></h2>
  <div class="abs promise">
    <p>We deliver first-class goods to the agreed place at the right time. We are friendly and close to the customer - just beverage dealers from tradition and with responsibility.</p>
    <p>In 1952 the company was realigned as a food retailer. In 1982 Konrad Lindner took over his father's grocery. In 1990 this grocery store became a FRISCHMARKT store, which is still part of the entire company. In 1994 Konrad Lindner opened his first beverage pick-up market with the "Drink Corner" in Brunnhain, and in 1995 he founded the beverage wholesaler Beverages Nordquell.</p>
  </div>
  <div class="abs girl" role="img" aria-label="Photo of a young woman with headphones drinking from a cup with a straw"></div>

  <h2 class="abs testi-h">Client testimonial</h2>
  <div class="abs card" style="left:127px">
    <div class="avatar" role="img" aria-label="Client photo"></div>
    <h3>Lena, 37</h3><div class="place">Jahre, Talwiese</div>
    <p>Quisque at magna eu augue semper euismod. Fusce commodo molestie luctus. Donec mollis nulla ipsum, vitae faucibus dui dapibus at. Cras ullamcorper eget ipsum vel volutpat. Phasellus rhoncus in sapien tincidunt mollis.</p>
  </div>
  <div class="abs card" style="left:460px">
    <div class="avatar" role="img" aria-label="Client photo"></div>
    <h3>Jonas, 32</h3><div class="place">Jahre, Talwiese</div>
    <p>Quisque at magna eu augue semper euismod. Fusce commodo molestie luctus. Donec mollis nulla ipsum, vitae faucibus dui dapibus at. Cras ullamcorper eget ipsum vel volutpat. Phasellus rhoncus in sapien tincidunt mollis.</p>
  </div>
  <div class="abs card" style="left:790px">
    <div class="avatar" role="img" aria-label="Client photo"></div>
    <h3>Clara, 32</h3><div class="place">Jahre, Talwiese</div>
    <p>Quisque at magna eu augue semper euismod. Fusce commodo molestie luctus. Donec mollis nulla ipsum, vitae faucibus dui dapibus at. Cras ullamcorper eget ipsum vel volutpat. Phasellus rhoncus in sapien tincidunt mollis.</p>
  </div>

  <div class="abs quick-h">Quicklinks</div>
  <div class="abs links" style="left:92px">Home<br>Companies<br>Team<br>Wholesale<br>All about your event</div>
  <div class="abs links" style="left:369px">Career<br>Downloads<br>Contact<br>Data protection / imprint</div>
  <div class="abs contact">
    <div class="row">
      <svg width="20" height="24" viewBox="0 0 20 24"><path d="M10 1C5 1 2 5 2 9c0 6 8 14 8 14s8-8 8-14c0-4-3-8-8-8z" fill="none" stroke="#1f6b5c" stroke-width="2"/><circle cx="10" cy="9" r="3" fill="none" stroke="#1f6b5c" stroke-width="2"/></svg>
      <div style="line-height:18px">Nordquell Getränke GmbH<br>Lindenweg 12<br>01234 Talwiese</div>
    </div>
    <div class="row" style="margin-top:16px">
      <svg width="20" height="20" viewBox="0 0 20 20"><path d="M4 1l4 4-2 3c1 3 3 5 6 6l3-2 4 4-3 3C8 19 1 12 1 4z" fill="#1f6b5c"/></svg>
      <div>+49 30000 11220</div>
    </div>
    <div class="row" style="margin-top:10px">
      <svg width="20" height="18" viewBox="0 0 20 18"><rect x="5" y="1" width="10" height="5" fill="#1f6b5c"/><rect x="1" y="6" width="18" height="8" rx="2" fill="#1f6b5c"/><rect x="5" y="12" width="10" height="5" fill="#fff" stroke="#1f6b5c" stroke-width="1.5"/></svg>
      <div>+49 30000 11221</div>
    </div>
  </div>
  <div class="abs stay">Stay Connected
    <div class="social"><span></span><span></span><span></span><span></span></div>
  </div>
</div>
</body>
</html>
```